Theme for a ChoreFalcon like site for Teenage Entrepreneurs

Design a theme that looks similar to the ChoreFalcon.com website that captures some of the look & feel of our live website (Junpreno.com).
We like the idea of illustrated people (cartoon), but are not 100% married to it.

We are building on top of a framework that has an existing structure and fairly usable layout that we also think would be good to retain.
You can view that framework here: https://gigmotor.blendloom.com/

This website is focused on 14 to 18 year old kids who do neighborhood work such as lawn care, cleanup, snow removal, pet care and baby sitting.

Attached is a powerpoint briefing with more specific details as well.

1. Review our live site Junpreno.com
2. Review ChoreFalcon.com
3. Review https://gigmotor.blendloom.com
4. Review our uploaded Powerpoint
5. Come up with awesome designs that we should use on our site!

Target Market(s)

Home owners in neighborhoods and 14 to 18 year old male / female entrepreneurs

Font styles to use
Sans Serif

Colors
0792cd
ffffff
fbf289
cfeae6

Requirements
Must have
• Design around the visible functions of the Chorefalcon.com and https://gigmotor.blendloom.com websites as a guide.
• Our site must retain those functions for the homeowner and the person doing the work.
Nice to have
• We like the idea of using illustrated people (the cartoon like characters) but we don't 100% need it. We would like to see some designs with illustrated people and without.

```html
<!DOCTYPE html>
<html lang="en">
<head>
<meta charset="utf-8">
<title>Junpreno – Creating Better Neighborhoods</title>
<link href="https://fonts.googleapis.com/css2?family=Josefin+Sans:wght@300;400;600;700&display=swap" rel="stylesheet">
<style>
  :root {
    --brand-blue: #0792cd;
    --white: #ffffff;
    --brand-yellow: #fbf289;
    --panel-mint: #cfeae6;
    --sky: #5fbbe0;
    --sky-light: #8fd0ea;
    --meadow: #8cc477;
    --meadow-mid: #9dcb72;
    --meadow-low: #c6d66f;
    --ink: #1f1f1f;
    --text-soft: rgba(255,255,255,0.92);
    --panel-text: #6b7a78;
  }
  * { box-sizing: border-box; margin: 0; padding: 0; }
  html, body { width: 1200px; height: 2200px; overflow: hidden; }
  body {
    position: relative;
    font-family: "Josefin Sans", "Helvetica Neue", Arial, sans-serif;
    color: var(--white);
    background: linear-gradient(180deg,
      var(--sky) 0px, var(--sky-light) 440px, var(--meadow) 600px,
      var(--meadow) 1100px, var(--meadow-mid) 1500px, var(--meadow-low) 2050px);
  }
  .top-rule { position: absolute; top: 0; left: 0; width: 1200px; height: 4px; background: var(--brand-yellow); }

  .hero-scene {
    position: absolute; top: 4px; left: 0; width: 1200px; height: 640px;
    background:
      radial-gradient(ellipse 180px 120px at 595px 470px, rgba(168,218,205,0.55), transparent 70%),
      linear-gradient(180deg, rgba(120,200,235,0.0) 0%, rgba(95,165,190,0.35) 62%, rgba(140,196,119,0.9) 82%, rgba(140,196,119,0) 100%);
  }

  .btn-outline, .btn-solid {
    position: absolute; top: 75px; height: 44px; border-radius: 22px;
    font-size: 15px; font-weight: 400; letter-spacing: 0.2px;
    display: flex; align-items: center; justify-content: center; text-transform: uppercase;
  }
  .btn-solid { left: 100px; width: 206px; background: var(--white); color: var(--brand-blue); }
  .btn-outline { left: 917px; width: 184px; border: 2px solid var(--white); color: var(--white); }

  .brand { position: absolute; top: 66px; left: 0; width: 1200px; text-align: center;
    font-size: 50px; font-weight: 700; color: var(--brand-yellow); letter-spacing: 1px; }
  .tagline { position: absolute; top: 142px; left: 0; width: 1200px; text-align: center;
    font-size: 21px; font-weight: 300; line-height: 36px; text-transform: uppercase; }

  .hero-title { position: absolute; top: 292px; left: 0; width: 1200px; text-align: center;
    font-size: 37px; font-weight: 600; color: var(--ink); }
  .hero-sub { position: absolute; top: 343px; left: 0; width: 1200px; text-align: center;
    font-size: 35px; font-weight: 600; }

  .chore-search { position: absolute; top: 408px; left: 305px; width: 590px; height: 48px; display: flex; }
  .chore-search .field { flex: 1; background: var(--white); color: #555; font-size: 14px; font-weight: 300;
    display: flex; align-items: center; padding-left: 24px; }
  .chore-search .go { width: 75px; background: var(--brand-blue); display: flex; align-items: center; justify-content: center; }

  .section-title-left { position: absolute; top: 642px; left: 100px; font-size: 30px; font-weight: 400; }
  .intro { position: absolute; top: 697px; left: 100px; width: 1000px; font-size: 17px; font-weight: 300;
    line-height: 34px; color: var(--text-soft); }

  .service { position: absolute; top: 793px; width: 190px; text-align: center; }
  .service .art { width: 173px; height: 173px; margin: 0 auto; border-radius: 50%;
    border: 4px solid #d7e39a; }
  .service .shadow { width: 150px; height: 10px; margin: 10px auto 0; border-radius: 50%;
    background: rgba(60,90,50,0.22); }
  .service .label { margin-top: 16px; font-size: 24px; font-weight: 400; color: var(--ink); }

  .divider { position: absolute; top: 1110px; left: 100px; width: 1000px; height: 1px; background: rgba(230,235,160,0.7); }

  .section-title { position: absolute; left: 0; width: 1200px; text-align: center; font-weight: 600; text-transform: uppercase; }
  .how-title { top: 1178px; font-size: 30px; }
  .how-copy { position: absolute; top: 1234px; left: 180px; width: 840px; text-align: center;
    font-size: 18px; font-weight: 300; line-height: 35px; color: var(--text-soft); }

  .better-panel { position: absolute; top: 1345px; left: 100px; width: 1002px; height: 400px; }
  .better-title { top: 1470px; font-size: 27px; color: var(--brand-blue); }
  .better-copy { position: absolute; top: 1521px; left: 170px; width: 860px; text-align: center;
    font-size: 15px; font-weight: 300; line-height: 34px; color: var(--panel-text); }

  .cta-copy { position: absolute; top: 1788px; left: 0; width: 1200px; text-align: center;
    font-size: 29px; font-weight: 400; line-height: 43px; }
  .cta-copy strong { font-weight: 700; }
  .btn-preview { position: absolute; top: 1901px; left: 516px; width: 168px; height: 45px; border-radius: 23px;
    background: var(--brand-blue); font-size: 14px; font-weight: 600; display: flex; align-items: center; justify-content: center; }

  .footer-rule { position: absolute; top: 2014px; left: 100px; width: 1000px; height: 1px; background: rgba(255,255,255,0.4); }
  .footer-links { position: absolute; top: 2050px; left: 100px; font-size: 13px; font-weight: 300; }
  .copyright { position: absolute; top: 2050px; right: 100px; font-size: 13px; font-weight: 300; }

  .meadow-strip { position: absolute; bottom: 0; left: 0; width: 1200px; height: 130px;
    background: linear-gradient(180deg, rgba(120,190,60,0) 0%, #6fb13e 45%, #4f9a2d 100%); }
</style>
</head>
<body>
  <div class="top-rule"></div>

  <div class="hero-scene" role="img" aria-label="Illustrated neighborhood scene: hot air balloons in a blue sky, clouds, mountains, a small house and trees on green hills"></div>

  <header>
    <a class="btn-solid">Homeowner Login</a>
    <div class="brand">JUNPRENO</div>
    <a class="btn-outline">Junpreno Login</a>
    <p class="tagline">Creating better neighborhoods<br>one kid at a time</p>
  </header>

  <section class="hero">
    <h1 class="hero-title">BECOME A JUNPRENO</h1>
    <p class="hero-sub">Let us help you build your tomorrow!</p>
    <div class="chore-search">
      <div class="field">What chore do you need help with?</div>
      <div class="go">
        <svg width="24" height="24" viewBox="0 0 24 24"><circle cx="10" cy="10" r="7" fill="none" stroke="#fff" stroke-width="3"/><line x1="15" y1="15" x2="21" y2="21" stroke="#fff" stroke-width="3.4" stroke-linecap="round"/></svg>
      </div>
    </div>
  </section>

  <section class="about">
    <h2 class="section-title-left">What is a JUNPRENO?</h2>
    <p class="intro">A JUNPRENO is an aspiring entrepreneur who is looking for exciting new ways to grow and build their business.<br>Some of the services that a Junpreno can offer to do for homeowners are:</p>

    <div class="service" style="left:87px">
      <div class="art" role="img" aria-label="Illustration of a teen mowing a lawn" style="background:linear-gradient(180deg,#bfe3f2 0%,#eef6f0 55%,#7cc04c 100%)"></div>
      <div class="shadow"></div><div class="label">Lawn Care</div>
    </div>
    <div class="service" style="left:294px">
      <div class="art" role="img" aria-label="Illustration of children playing in a toy-filled room" style="background:linear-gradient(180deg,#f2d36b 0%,#e8a458 50%,#5aa9c9 100%)"></div>
      <div class="shadow"></div><div class="label">Baby Sitting</div>
    </div>
    <div class="service" style="left:499px">
      <div class="art" role="img" aria-label="Illustration of a busy person juggling household chores" style="background:linear-gradient(180deg,#5fb9d3 0%,#4aa6c2 100%)"></div>
      <div class="shadow"></div><div class="label">Household Chores</div>
    </div>
    <div class="service" style="left:705px">
      <div class="art" role="img" aria-label="Illustration of a dog and cat beside a doghouse" style="background:linear-gradient(180deg,#f1f0ea 0%,#c98d55 60%,#8fc46a 100%)"></div>
      <div class="shadow"></div><div class="label">Pet Care</div>
    </div>
    <div class="service" style="left:911px">
      <div class="art" role="img" aria-label="Illustration of a snow plough clearing snow" style="background:linear-gradient(180deg,#4f8fb3 0%,#8fbfd6 55%,#e3b24a 100%)"></div>
      <div class="shadow"></div><div class="label">Snow Removal</div>
    </div>
  </section>

  <div class="divider"></div>

  <section class="how">
    <h2 class="section-title how-title">How does it work?</h2>
    <p class="how-copy">JUNPRENO is a platform to help you build your business from the ground up. It will also help you find jobs in your area by connecting you to local home owners seeking help for various services.</p>
  </section>

  <section class="better">
    <svg class="better-panel" viewBox="0 0 1002 400" preserveAspectRatio="none" aria-hidden="true">
      <path d="M0 2 Q501 80 1002 0 L1002 398 Q501 320 0 400 Z" fill="var(--panel-mint)"/>
    </svg>
    <h2 class="section-title better-title">What makes us better than the next guy?</h2>
    <p class="better-copy">On top of providing you with a network to find local jobs in your community, we will work with you to help you become an entrepreneur. We will link you to stepping stones such as: resources, tools and webinars to build and grow your business. We will also provide a link to a community of other JUNPRENOS to build business connections in your area.</p>
  </section>

  <section class="cta">
    <p class="cta-copy">Still not sure? Connect with other <strong>JUNPRENOS</strong> to see how it has<br>helped them grow their businesses!</p>
    <a class="btn-preview">PREVIEW &gt;&gt;</a>
  </section>

  <footer>
    <div class="footer-rule"></div>
    <div class="footer-links">About us | contact us | press | Terms &amp; policy</div>
    <div class="copyright">© Copyright 2017 JUNPRENO All Rights Reserved</div>
  </footer>

  <div class="meadow-strip" role="img" aria-label="Illustrated grass border with white daisies"></div>
</body>
</html>
```